Redesign of WordHarbor.com in Bootstrap 4

Current design of WordHarbor.com is not responsive. We need to change it to latest version of Bootstrap 4 keeping essential elements in place.

Apart from home page, we need designs for http://www.wordharbor.com/meaning/cat also.

Coding

Coded - Design and coding required

Number of Pages Required

2 page

Colors
34a7d8

Requirements
Must have
• Bootstrap 4

```html
<!DOCTYPE html>
<html lang="en">
<head>
<meta charset="utf-8">
<title>WordHarbor – Meaning of Cat</title>
<link href="https://fonts.googleapis.com/css2?family=Raleway:wght@400;500;600;700&family=Lato:wght@400;700&display=swap" rel="stylesheet">
<style>
:root{
  --orange:#f7931e;
  --ink:#1f1f1f;
  --text:#333;
  --rule:#d9dee4;
  --panel:#f4f8fc;
  --panel-line:#cfe0ee;
  --panel-head:#dbe9f5;
  --band:#e6eff7;
  --blue:#1a6fb5;
  --brand-blue:#34a7d8;
  --footer:#262626;
  --footer-deep:#1b1b1b;
  --white:#fff;
}
*{box-sizing:border-box;margin:0;padding:0}
html,body{width:1200px;height:2174px;overflow:hidden;background:var(--white)}
body{position:relative;font-family:'Lato',Arial,sans-serif;color:var(--text)}
.abs{position:absolute}

/* header */
.site-header{left:0;top:0;width:1200px;height:83px;background:var(--white);border-bottom:1px solid #e4e4e4}
.brand{left:149px;top:22px;display:flex;align-items:center;gap:8px;font-family:'Raleway',sans-serif;font-weight:700;font-size:24px;color:var(--ink)}
.brand-dot{width:14px;height:14px;background:var(--orange)}
.nav{left:332px;top:0;height:83px;display:flex;font-family:'Raleway',sans-serif;font-weight:600;font-size:12px;color:#555}
.nav a{display:flex;align-items:center;height:83px;color:inherit;text-decoration:none;padding:0 27px;border-right:1px solid #e6e6e6}
.nav a:last-child{border-right:none}
.nav a.active{background:var(--orange);color:var(--white);padding:0 17px}
.btn-join{left:953px;top:30px;width:97px;height:27px;background:#222;color:var(--white);font-family:'Raleway',sans-serif;font-weight:700;font-size:11.5px;display:flex;align-items:center;justify-content:center;border-radius:2px}

/* hero */
.hero{left:0;top:83px;width:1200px;height:268px;background:linear-gradient(180deg,#b8cc1e 0%,#d4dc6a 45%,#ece9c8 80%,#f2e6cf 100%)}
.hero-art{right:0;top:0;width:560px;height:268px;background:linear-gradient(200deg,#f3d9a0 0%,#e8c27a 45%,#d9a75a 75%,#e0573c 92%,#f0ece4 100%)}
.hero-title{left:149px;top:20px;font-family:'Raleway',sans-serif;font-weight:700;font-size:25px;color:var(--ink)}
.hero-list{left:149px;top:62px;list-style:none;font-family:'Raleway',sans-serif;font-weight:500;font-size:15px;color:#222;width:400px}
.hero-list li{display:flex;gap:6px;margin-bottom:14px;line-height:18px}
.hero-list li:nth-child(4){margin-bottom:10px}
.hero-list svg{flex:none;margin-top:2px}
.hero-list a{color:var(--blue);font-weight:700}

/* breadcrumb */
.crumbs{left:0;top:353px;width:1200px;height:39px;background:var(--band);font-family:'Raleway',sans-serif;font-size:12px;color:#666;padding:12px 0 0 151px}
.crumbs b{color:var(--orange);font-weight:700}

/* search */
.search-card{left:149px;top:416px;width:593px;height:117px;border:1px solid var(--panel-line);background:var(--white);border-radius:2px}
.search-input{left:16px;top:14px;width:416px;height:42px;border:1px solid #ccd6e0;border-radius:3px;padding:11px 13px;font-size:15px;color:#555}
.search-btn{left:448px;top:14px;width:130px;height:42px;background:var(--orange);border-radius:3px;color:#111;font-family:'Raleway',sans-serif;font-weight:700;font-size:15px;display:flex;align-items:center;justify-content:center}
.search-hint{left:22px;top:63px;font-family:'Raleway',sans-serif;font-size:13px;color:#555}
.search-term{left:23px;top:85px;font-family:'Raleway',sans-serif;font-weight:700;font-size:15px;color:#111}

.summary{left:150px;top:558px;width:592px;font-size:13px;color:#222;white-space:nowrap;overflow:hidden;display:flex;gap:7px;align-items:center;font-family:'Raleway',sans-serif}
.summary svg{flex:none}

/* meanings panel */
.meanings{left:150px;top:590px;width:592px;height:665px;background:var(--panel);border:1px solid var(--panel-line)}
.section-head{position:absolute;left:9px;width:574px;height:26px;background:var(--panel-head);font-family:'Raleway',sans-serif;font-size:13px;font-weight:400;color:#111;padding:5px 7px}
.section-head b{font-weight:700}
.def-list{position:absolute;left:9px;width:560px;list-style:none;font-size:11px;line-height:24px;color:#333}
.def-list li{display:flex}
.def-list .n{width:24px;flex:none}
.ad-slot{position:absolute;top:467px;width:225px;height:187px;background:linear-gradient(160deg,#d7d2cc 0%,#b89a80 55%,#2b2b2b 100%)}

/* related list */
.related{left:150px;top:1276px;width:592px;list-style:none;font-size:11px;color:#333}
.related li{height:23.9px;line-height:22px;border-bottom:1px solid var(--rule);white-space:nowrap;overflow:hidden;text-overflow:ellipsis;padding-left:2px}

/* browse */
.browse-title{left:158px;top:1866px;font-family:'Raleway',sans-serif;font-weight:600;font-size:12px;color:#333}
.browse{left:150px;top:1890px;width:592px;height:43px;background:var(--panel);border:1px solid var(--panel-line);display:flex;gap:4px;padding:12px 0 0 11px}
.browse span{width:18px;height:17px;border:1px solid #b9c6d2;background:var(--white);font-size:9px;color:#555;display:flex;align-items:center;justify-content:center}
.browse span.on{border-color:var(--orange);color:var(--orange)}

/* sidebar */
.sidebar{left:765px;top:414px;width:284px;height:1515px;background:var(--panel);border:1px solid var(--panel-line)}
.wotd{left:15px;top:23px;width:255px;height:154px;background:var(--white);border:1px solid #cfd6dd}
.wotd-head{height:32px;background:#2b2b2b;color:var(--white);font-family:'Raleway',sans-serif;font-weight:600;font-size:15px;padding:6px 17px}
.wotd-word{left:17px;top:51px;font-family:'Raleway',sans-serif;font-size:16px;color:#333}
.wotd-speak{left:213px;top:54px;width:24px;height:24px;border-radius:50%;background:#dbe6f0;display:flex;align-items:center;justify-content:center}
.wotd-src{left:20px;top:86px;font-family:'Raleway',sans-serif;font-size:12.5px;color:#777}
.wotd-foot{left:0;bottom:0;width:253px;height:32px;background:#eef3f8;border-top:1px solid #d7e0e8}
.share{position:absolute;top:10px;width:16px;height:16px;border-radius:2px}
.show-def{position:absolute;right:4px;top:6px;width:110px;height:22px;background:#1e6fbd;color:var(--white);font-family:'Raleway',sans-serif;font-weight:600;font-size:12px;display:flex;align-items:center;justify-content:center}
.side-ad{left:35px;top:195px;width:214px;height:178px;background:linear-gradient(135deg,#3a5760 0%,#6a7f80 50%,#c2c0b4 100%)}
.side-ad-title{position:absolute;left:12px;top:14px;font-family:'Raleway',sans-serif;font-weight:700;font-size:18px;color:var(--white);width:190px;line-height:20px}

/* footer */
.footer{left:0;top:1969px;width:1200px;height:161px;background:var(--footer);border-top:4px solid var(--orange)}
.fcol{position:absolute;top:25px;width:182px;font-family:'Raleway',sans-serif;color:#ddd}
.fcol h4{font-size:13px;font-weight:700;color:var(--white);padding-bottom:9px;border-bottom:1px solid #444;margin-bottom:11px}
.fcol ul{list-style:none;font-size:11.5px}
.fcol li{margin-bottom:9px}
.fcol li::before{content:"•";margin-right:9px}
.fbrand{left:836px;top:18px;width:206px;text-align:center;font-family:'Raleway',sans-serif;color:var(--white);border-left:1px solid #3a3a3a;height:110px}
.fbrand .name{font-size:22px;font-weight:700;color:#bdbdbd;margin:10px 0 12px}
.fbrand p{font-size:10.5px;line-height:14px;color:#ddd}
.tagline{left:149px;top:2108px;font-family:'Raleway',sans-serif;font-size:14px;color:var(--orange)}
.bottom-bar{left:0;top:2130px;width:1200px;height:44px;background:var(--footer-deep);font-family:'Raleway',sans-serif;font-size:11px;color:#ccc;padding:14px 0 0 151px}
</style>
</head>
<body>

<header class="site-header abs">
  <div class="brand abs"><span class="brand-dot"></span>WordHarbor</div>
  <nav class="nav abs">
    <a class="active" href="#">Home</a>
    <a href="#">Idioms</a>
    <a href="#">Crossword</a>
    <a href="#">Comman Errors</a>
    <a href="#">Blog</a>
    <a href="#">Contact</a>
  </nav>
  <div class="btn-join abs">Join For FREE</div>
</header>

<section class="hero abs">
  <div class="hero-art abs" role="img" aria-label="Open book with fanned pages on a warm background"></div>
  <h1 class="hero-title abs">Search, Save and Master Words</h1>
  <ul class="hero-list abs">
    <li><svg width="14" height="14" viewBox="0 0 14 14"><rect x="1" y="1" width="12" height="12" fill="none" stroke="#222" stroke-width="1.4"/><path d="M3 7l3 3 6-8" fill="none" stroke="#222" stroke-width="2"/></svg>Search From More Than 300,000 Words And Phrases</li>
    <li><svg width="14" height="14" viewBox="0 0 14 14"><rect x="1" y="1" width="12" height="12" fill="none" stroke="#222" stroke-width="1.4"/><path d="M3 7l3 3 6-8" fill="none" stroke="#222" stroke-width="2"/></svg>Multiple Usages To Clarify The Context</li>
    <li><svg width="14" height="14" viewBox="0 0 14 14"><rect x="1" y="1" width="12" height="12" fill="none" stroke="#222" stroke-width="1.4"/><path d="M3 7l3 3 6-8" fill="none" stroke="#222" stroke-width="2"/></svg>Audio, Phonetics, Meanings, Synonyms And Antonyms</li>
    <li><svg width="14" height="14" viewBox="0 0 14 14"><rect x="1" y="1" width="12" height="12" fill="none" stroke="#222" stroke-width="1.4"/><path d="M3 7l3 3 6-8" fill="none" stroke="#222" stroke-width="2"/></svg>Save The Words To Your Personal Deck And Access From Anywhere</li>
    <li><svg width="14" height="14" viewBox="0 0 14 14"><rect x="1" y="1" width="12" height="12" fill="none" stroke="#222" stroke-width="1.4"/><path d="M3 7l3 3 6-8" fill="none" stroke="#222" stroke-width="2"/></svg>It's&nbsp;<a href="#">Free</a></li>
  </ul>
</section>

<div class="crumbs abs">Home &gt;&gt; <b>Meaning</b></div>

<main>
  <div class="search-card abs">
    <div class="search-input abs">Cat</div>
    <div class="search-btn abs">Search</div>
    <div class="search-hint abs">eg. (tattoo, tone, hindu )</div>
    <div class="search-term abs">Cat</div>
  </div>

  <p class="summary abs">Cat
    <svg width="14" height="12" viewBox="0 0 14 12"><path d="M1 4h3l4-3v10L4 8H1z" fill="#222"/><path d="M10 3c1.5 1.5 1.5 4.5 0 6M12 1.5c2.5 2.5 2.5 6.5 0 9" fill="none" stroke="#222" stroke-width="1.2"/></svg>
    <span>'kæt/ ?&nbsp; feline mammal usually having thick soft fur and no ability to roar: domestic cats;...</span></p>

  <section class="meanings abs">
    <h2 class="section-head" style="top:11px"><b>cat</b> meaning(s</h2>
    <ol class="def-list" style="top:47px">
      <li><span class="n">1.</span>(n) feline mammal usually having thick soft fur and no ability to roar: domestic cats; wildcats</li>
      <li><span class="n">2.</span>(n) an informal term for a youth or man</li>
      <li><span class="n">3.</span>(n) a spiteful woman gossip</li>
      <li><span class="n">4.</span>(n) the leaves of the shrub Catha edulis which are chewed like tobacco or used to make tea; has the<br>effect of a euphoric stimulant</li>
      <li><span class="n">5.</span>(n) a whip with nine knotted cords</li>
      <li><span class="n">6.</span>(n) a large tracked vehicle that is propelled by two endless metal belts; frequently used for moving<br>earth in construction and farm work</li>
      <li><span class="n">7.</span>(n) any of several large cats typically able to roar and living in the wild</li>
      <li><span class="n">8.</span>(n) a method of examining body organs by scanning them with X rays and using a computer to construct<br>a series of cross-sectional scans along a single axis</li>
      <li><span class="n">9.</span>(v) beat with a cat-o'-nine-tails</li>
      <li><span class="n">10.</span>(v) eject the contents of the stomach through the mouth</li>
    </ol>
    <h2 class="section-head" style="top:375px"><b>cat</b> usage(s)</h2>
    <ol class="def-list" style="top:410px">
      <li><span class="n">1.</span>Wire Desk: Wildlife reserves alone cannot protect big cats.</li>
      <li><span class="n">2.</span>Studies show that the company of a cat can help keep you calm and happy.</li>
    </ol>
    <div class="ad-slot" style="left:8px" role="img" aria-label="Summit Circle advertisement with portrait and call to action"></div>
    <div class="ad-slot" style="left:280px" role="img" aria-label="Summit Circle advertisement with portrait and call to action"></div>
  </section>

  <ul class="related abs">
    <li>cat and mouse cat and mouse&nbsp; a game for children in which the players form a circle and join hands;...</li>
    <li>cat and rat cat and rat&nbsp; a game for children in which the players form a circle and join hands; they...</li>
    <li>cat bear cat bear&nbsp; reddish-brown Old World raccoon-like carnivore; in some classifications considered...</li>
    <li>cat box cat box&nbsp; a receptacle for cat excrement</li>
    <li>cat burglar cat burglar&nbsp; a burglar who unlawfully breaks into and enters another person's house</li>
    <li>cat cracker cat cracker&nbsp; a chemical reactor for converting oils with high boiling points into fuels...</li>
    <li>cat fancier cat fancier&nbsp; a person who breeds and cares for cats</li>
    <li>cat flea cat flea&nbsp; flea that breeds chiefly on cats and dogs and rats</li>
    <li>cat food cat food&nbsp; food prepared for cats</li>
    <li>cat rig cat rig&nbsp; rig of a catboat</li>
    <li>cat scan cat scan&nbsp; an image produced by scanning</li>
    <li>cat scanner cat scanner&nbsp; a tomograph that constructs a 3-D model of an object by combining parallel...</li>
    <li>cat scratch disease cat scratch disease&nbsp; a disease thought to be transmitted to humans by a scratch from...</li>
    <li>cat shark cat shark&nbsp; small bottom-dwelling sharks with cat-like eyes; found along continental slopes</li>
    <li>cat sleep cat sleep&nbsp; sleeping for a short period of time (usually not in bed)</li>
    <li>cat squirrel cat squirrel&nbsp; common reddish-brown squirrel of Europe and parts of Asia</li>
    <li>cat suit cat suit&nbsp; a tight-fitting garment of stretchy material that covers the body from the shoulders...</li>
    <li>cat thyme cat thyme&nbsp; Mediterranean germander having small hairy leaves and reddish purple flowers;...</li>
    <li>cat valium cat valium&nbsp; street names for ketamine</li>
    <li>cat's cradle cat's cradle&nbsp; a game played with string looped over the fingers</li>
    <li>cat's eye cat's eye&nbsp; any of various gems (as chrysoberyl or chalcedony) that reflect light when cut...</li>
    <li>cat's feet cat's feet&nbsp; low-growing perennial herb having leaves with whitish down and clusters of...</li>
    <li>cat's foot cat's foot&nbsp; low-growing perennial herb having leaves with whitish down and clusters of...</li>
  </ul>

  <h3 class="browse-title abs">Browse Dictionary</h3>
  <div class="browse abs">
    <span class="on">A</span><span>B</span><span>C</span><span>D</span><span>E</span><span>F</span><span>G</span><span>H</span><span>I</span><span>J</span><span>K</span><span>L</span><span>M</span><span>N</span><span>O</span><span>P</span><span>Q</span><span>R</span><span>S</span><span>T</span><span>U</span><span>V</span><span>W</span><span>Y</span><span>X</span><span>Z</span>
  </div>
</main>

<aside class="sidebar abs">
  <div class="wotd abs">
    <div class="wotd-head">Word of the Day</div>
    <div class="wotd-word abs">Ascendancy</div>
    <div class="wotd-speak abs"><svg width="12" height="10" viewBox="0 0 14 12"><path d="M1 4h3l4-3v10L4 8H1z" fill="#1e6fbd"/><path d="M10 3c1.5 1.5 1.5 4.5 0 6" fill="none" stroke="#1e6fbd" stroke-width="1.4"/></svg></div>
    <div class="wotd-src abs">/ From the sen si /</div>
    <div class="wotd-foot abs">
      <span class="share" style="left:16px;background:var(--brand-blue)"></span>
      <span class="share" style="left:38px;background:#f26b1d"></span>
      <span class="show-def">Show Definition</span>
    </div>
  </div>
  <div class="side-ad abs" role="img" aria-label="Main Street Brief newsletter advertisement with office scene">
    <div class="side-ad-title">MAIN STREET BRIEF</div>
  </div>
</aside>

<footer class="footer abs">
  <div class="fcol" style="left:151px">
    <h4>WordHarbor</h4>
    <ul><li>FAQ</li><li>Contact</li><li>Blog</li></ul>
  </div>
  <div class="fcol" style="left:381px">
    <h4>Legal</h4>
    <ul><li>Privacy Policy</li><li>Terms of Use</li></ul>
  </div>
  <div class="fcol" style="left:613px">
    <h4>Others</h4>
    <ul><li>Popular Words</li><li>Common Errors in English</li><li>Exam Prep Online</li></ul>
  </div>
  <div class="fbrand abs">
    <div class="name">WordHarbor</div>
    <p><b>WordHarbor Dictionary:</b><br>Meaning/Definition, Audio, Phonetics,<br>Usages and more</p>
  </div>
</footer>
<div class="tagline abs">WordHarbor Dictionary: Meaning/Definition, Audio, Phonetics, Usages and more</div>
<div class="bottom-bar abs">Copyright © 2016 Lexora Solutions Pvt. Ltd. All rights reserved.</div>

</body>
</html>
```